Jubo Application for Cars Accidents Services

We need app screen designs for company provide services for the cars that got accidents, the design should be modern official and simple, the pages around 26 include login, register, auth code, home, splash, request service, profile, settings, booking, booking info ..., we need something so professional please.

Target Market(s)

Cars owners

```html
<!DOCTYPE html>
<html lang="en">
<head>
<meta charset="UTF-8">
<title>Jubo – Authenticate Your Account</title>
<link href="https://fonts.googleapis.com/css2?family=Roboto:wght@400;500;700&display=swap" rel="stylesheet">
<style>
  :root {
    --brand-green: #7dc87b;
    --white: #ffffff;
    --digit-grey: #b8b8b8;
    --ink: #1f1f1f;
    --box-shadow: rgba(0, 0, 0, 0.08);
    --shield-blue: #8fdde8;
    --shield-yellow: #f4df3a;
  }
  * { margin: 0; padding: 0; box-sizing: border-box; }
  html, body {
    width: 1200px;
    height: 2598px;
    overflow: hidden;
    background: var(--white);
    font-family: "Roboto", sans-serif;
  }
  .screen {
    position: relative;
    width: 1200px;
    height: 2598px;
    background: var(--white);
  }
  .top-bar {
    position: absolute;
    left: 0; top: 0;
    width: 1200px; height: 205px;
    background: var(--brand-green);
    border-radius: 0 0 45px 45px;
  }
  .back-button {
    position: absolute;
    left: 96px; top: 72px;
    width: 64px; height: 64px;
  }
  .screen-title {
    position: absolute;
    left: 0; right: 0; top: 74px;
    text-align: center;
    color: var(--white);
    font-weight: 700;
    font-size: 51px;
    line-height: 60px;
    padding-left: 10px;
  }
  .security-illustration {
    position: absolute;
    left: 378px; top: 410px;
    width: 448px; height: 440px;
    border-radius: 40px;
    background: linear-gradient(160deg, var(--shield-blue) 0%, #bfe6a8 60%, var(--shield-yellow) 100%);
  }
  .auth-heading {
    position: absolute;
    left: 349px; top: 1010px;
    color: var(--brand-green);
    font-weight: 700;
    font-size: 77px;
    line-height: 112px;
  }
  .code-inputs {
    position: absolute;
    left: 173px; top: 1408px;
    display: flex;
    gap: 45px;
  }
  .code-digit {
    width: 179px; height: 179px;
    background: var(--white);
    border-radius: 10px;
    box-shadow: 0 3px 14px var(--box-shadow);
    display: flex;
    align-items: center;
    justify-content: center;
    color: var(--digit-grey);
    font-size: 77px;
    font-weight: 400;
  }
  .submit-button {
    position: absolute;
    left: 205px; top: 1779px;
    width: 793px; height: 154px;
    border-radius: 77px;
    background: var(--brand-green);
    box-shadow: 0 12px 22px rgba(0, 0, 0, 0.18);
    display: flex;
    align-items: center;
    justify-content: center;
    color: var(--white);
    font-size: 56px;
    font-weight: 500;
  }
  .bottom-nav {
    position: absolute;
    left: 0; bottom: 0;
    width: 1200px; height: 259px;
    background: var(--brand-green);
    border-radius: 45px 45px 0 0;
  }
  .nav-item {
    position: absolute;
    top: 50px;
    width: 360px;
    margin-left: -180px;
    display: flex;
    flex-direction: column;
    align-items: center;
    color: var(--ink);
    font-size: 51px;
    line-height: 60px;
  }
  .nav-item svg { width: 77px; height: 77px; margin-bottom: 18px; }
  .nav-garage { left: 218px; }
  .nav-directory { left: 602px; }
  .nav-quotes { left: 979px; }
</style>
</head>
<body>
<main class="screen">
  <header class="top-bar">
    <svg class="back-button" viewBox="0 0 24 24" fill="none" stroke="#ffffff" stroke-width="3" stroke-linecap="round" stroke-linejoin="round" aria-label="Back">
      <path d="M20 12H4M11 5l-7 7 7 7"/>
    </svg>
    <h1 class="screen-title">jubo</h1>
  </header>

  <div class="security-illustration" role="img" aria-label="Illustration of a user inside a security shield with a green check mark"></div>

  <h2 class="auth-heading">Authenticate<br>Your Account</h2>

  <div class="code-inputs">
    <div class="code-digit">0</div>
    <div class="code-digit">0</div>
    <div class="code-digit">0</div>
    <div class="code-digit">0</div>
  </div>

  <div class="submit-button">Go</div>

  <nav class="bottom-nav">
    <div class="nav-item nav-garage">
      <svg viewBox="0 0 24 24" fill="none" stroke="#1f1f1f" stroke-width="1.6" stroke-linejoin="round">
        <path d="M3 11l9-8 9 8M5 9.5V21h5v-6h4v6h5V9.5"/>
      </svg>
      <span>My Garage</span>
    </div>
    <div class="nav-item nav-directory">
      <svg viewBox="0 0 24 24" fill="none" stroke="#1f1f1f" stroke-width="1.6">
        <path d="M12 22s-7-7.2-7-12.5A7 7 0 0 1 19 9.5C19 14.8 12 22 12 22z"/>
        <circle cx="12" cy="9.5" r="2.6"/>
      </svg>
      <span>Directory</span>
    </div>
    <div class="nav-item nav-quotes">
      <svg viewBox="0 0 24 24" fill="none" stroke="#1f1f1f" stroke-width="1.8" stroke-linejoin="round">
        <path d="M3 5h7v7c0 4-2 6-5 7l-.8-1.6C6 16.4 7 15 7 13H3z"/>
        <path d="M14 5h7v7c0 4-2 6-5 7l-.8-1.6C17 16.4 18 15 18 13h-4z"/>
      </svg>
      <span>Quotes</span>
    </div>
  </nav>
</main>
</body>
</html>
```